Author needs a new book, Kindle and Audiobook cover design

I updated and re-edited a book I wrote 25 years ago but now realize the title and design did not get the job done. I am seeking a book, Kindle and audiobook design that will make me stand out. The final design will pop while being sensitive to the nature of the subject. The title of the book is Quiet Lanterns. Subtitle: Ways to Notice and Step Away From Harmful Circles While Keeping Steady Belief by Dorian T. Wexcombe. I am wanting to get the attention of people who have been damaged by a church relationship that started well but ended badly.
Updates

The book title is: Quiet Lanterns. The Subtitle is: Ways To Notice and Step Away From Harmful Circles While Keeping Steady Belief. The dimension is 6x9 (150 pages) and I am the author: Dorian T. Wexcombe

Target Market(s)

People with a church experience; church leadership. Religious abuse victims.

Industry/Entity Type

Christian

Font styles to use
Serif

Colors

Designer to choose colors to be used in the design.

Requirements
Nice to have
• I am not married to the Serif font if another design works better.

```html
<!DOCTYPE html>
<html lang="en">
<head>
<meta charset="UTF-8">
<title>Quiet Lanterns — Dorian T. Wexcombe</title>
<link href="https://fonts.googleapis.com/css2?family=Poppins:wght@600;700&display=swap" rel="stylesheet">
<style>
  :root {
    --sky-top: #cfe6ee;
    --sky-mid: #eef6f4;
    --glow: #fff6d8;
    --sun: #f7d772;
    --amber: #eea94a;
    --meadow: #5f7f3c;
    --meadow-dark: #34501f;
    --title-yellow: #f3c21c;
    --subtitle-teal: #3e8d92;
    --author-white: #ffffff;
  }
  html, body {
    margin: 0;
    padding: 0;
    width: 751px;
    height: 1200px;
    overflow: hidden;
    background: #ffffff;
  }
  .cover {
    position: relative;
    width: 751px;
    height: 1200px;
    overflow: hidden;
    font-family: "Poppins", sans-serif;
    text-align: center;
  }
  .cover-art {
    position: absolute;
    inset: 0;
    background:
      radial-gradient(ellipse 420px 360px at 50% 790px, var(--glow) 0%, rgba(255,246,216,0.7) 40%, rgba(255,246,216,0) 75%),
      radial-gradient(ellipse 300px 200px at 250px 830px, rgba(238,169,74,0.55) 0%, rgba(238,169,74,0) 80%),
      linear-gradient(to bottom,
        var(--sky-top) 0%,
        var(--sky-mid) 35%,
        #f7f3e2 55%,
        var(--sun) 70%,
        #e8c263 80%,
        var(--meadow) 90%,
        var(--meadow-dark) 100%);
  }
  .title {
    position: absolute;
    top: 62px;
    left: 0;
    right: 0;
    margin: 0;
    color: var(--title-yellow);
    font-weight: 700;
    font-size: 112px;
    line-height: 124px;
    letter-spacing: 2px;
    text-transform: uppercase;
  }
  .subtitle {
    position: absolute;
    top: 362px;
    left: 50px;
    right: 50px;
    margin: 0;
    color: var(--subtitle-teal);
    font-weight: 600;
    font-size: 26px;
    line-height: 35px;
    letter-spacing: 0.5px;
    text-transform: uppercase;
  }
  .author {
    position: absolute;
    top: 1118px;
    left: 0;
    right: 0;
    margin: 0;
    color: var(--author-white);
    font-weight: 700;
    font-size: 40px;
    line-height: 48px;
    letter-spacing: 1px;
    text-transform: uppercase;
  }
</style>
</head>
<body>
  <main class="cover">
    <div class="cover-art" role="img" aria-label="Silhouette of a person with arms raised against a bright sunrise sky over a grassy meadow, with birds in flight"></div>
    <h1 class="title">Quiet<br>Lanterns</h1>
    <p class="subtitle">Ways to Notice and Step Away From<br>Harmful Circles While Keeping<br>Steady Belief</p>
    <p class="author">Dorian T. Wexcombe</p>
  </main>
</body>
</html>
```